Sunporch Tidy Works half fold brochure design

I need a brochure for a new company. The name of the company is Sunporch Tidy Works. I am a Professional Organizer. I am requesting a one fold brochure 11" wide x 8.5" high (obviously once folded 5.5" wide x 8.5" high) brochure. I have been told this may need to be designed as a flyer? I have attached a VERY BASIC layout of what I think I am looking for. I have also attached the original logos in all the different formats I have. I would like to have a very light green background & the text I have in orange please make orange. PLEASE feel free to add color to my "Sunporch Tidy Works" logo's and use light/soft green & orange shades if possible (OK to go darker for BOLD purposes) The brochure DOES NOT have to stick to this layout, again just what I THINK I want :) - THANK YOU

EDIT: 01-21-15 Remove MARGARET BELDANE from all 3 places (front, bottom inside right & back) Remove just the BELDANE from the 1st line on the back. PRIVACY & ETHICS on the back, please remove "PRIVACY &", leave Ethics and the 1st line of the text under it. Please remove all of the text following the 1st sentence. THANK YOU

```html
<!DOCTYPE html>
<html lang="en">
<head>
<meta charset="utf-8">
<title>Sunporch Tidy Works – Brochure</title>
<link rel="stylesheet" href="https://fonts.googleapis.com/css2?family=Fira+Sans:ital,wght@0,400;1,400;1,600&family=Fira+Sans+Condensed:wght@500;600;700&display=swap">
<style>
  :root {
    --orange: #de8230;
    --orange-soft: #ebb886;
    --peach: #f5dabd;
    --sage: #eef3e2;
    --ink: #2f2f2f;
    --white: #ffffff;
    --badge: #e3e6dc;
  }
  * { margin: 0; padding: 0; box-sizing: border-box; }
  html, body { width: 1200px; height: 928px; overflow: hidden; background: var(--white); }
  body { position: relative; font-family: "Fira Sans", sans-serif; color: var(--ink); }
  .block { position: absolute; }

  /* inside left: greeting */
  .hello-band { left: 0; top: 0; width: 600px; height: 80px; background: var(--orange); }
  .hello-title { left: 34px; top: 8px; font-family: "Fira Sans Condensed", sans-serif; font-weight: 700; font-size: 50px; color: var(--white); letter-spacing: 1px; }
  .intro-panel { left: 0; top: 80px; width: 600px; height: 355px; background: var(--sage); border-right: 1px solid #e4e8da; }
  .intro-name { left: 35px; top: 100px; font-style: italic; font-weight: 600; font-size: 16px; color: var(--orange); }
  .intro-copy { left: 35px; top: 128px; width: 475px; font-style: italic; font-size: 14px; line-height: 22px; letter-spacing: -0.3px; }
  .intro-copy p + p { margin-top: 20px; }

  /* back: contact card */
  .card-panel { left: 0; top: 448px; width: 600px; height: 219px; background: var(--peach); }
  .card-tab { left: 235px; top: 437px; width: 365px; height: 86px; background: var(--orange); }
  .card-tab-text { left: 256px; top: 473px; font-family: "Fira Sans Condensed", sans-serif; font-weight: 500; font-size: 20px; color: var(--white); }
  .card-name { left: 40px; top: 520px; width: 200px; font-family: "Fira Sans Condensed", sans-serif; font-weight: 600; font-size: 36px; line-height: 40px; color: var(--orange); }
  .card-contact { left: 250px; top: 550px; width: 280px; text-align: center; font-size: 16px; line-height: 24px; }

  .rule-orange { left: 0; top: 678px; width: 600px; height: 4px; background: var(--orange); }
  .member-badge { left: 42px; top: 715px; }
  .ethics-title { left: 265px; top: 764px; width: 280px; text-align: center; font-family: "Fira Sans Condensed", sans-serif; font-weight: 500; font-size: 20px; color: var(--orange); }
  .ethics-copy { left: 255px; top: 796px; width: 300px; text-align: center; font-size: 16px; line-height: 24px; }
  .rule-peach { left: 0; top: 880px; width: 600px; height: 4px; background: var(--peach); }

  /* cover */
  .cover-panel { left: 615px; top: 15px; width: 568px; height: 400px; background: var(--sage); }
  .cover-name { left: 615px; top: 130px; width: 568px; text-align: center; font-family: "Fira Sans Condensed", sans-serif; font-weight: 600; font-size: 70px; line-height: 80px; color: var(--orange); }
  .cover-band { left: 600px; top: 435px; width: 600px; height: 90px; background: var(--orange); }
  .cover-band-text { left: 600px; top: 455px; width: 600px; text-align: center; font-family: "Fira Sans Condensed", sans-serif; font-weight: 600; font-size: 37px; color: var(--white); }
  .cover-contact-panel { left: 600px; top: 540px; width: 452px; height: 255px; background: var(--orange-soft); }
  .cover-contact { left: 600px; top: 596px; width: 452px; text-align: center; font-size: 16px; line-height: 25px; }
  .cover-contact .gap { margin-top: 26px; }
  .cover-side { left: 1070px; top: 540px; width: 130px; height: 255px; background: var(--sage); }
  .definition-panel { left: 600px; top: 812px; width: 600px; height: 72px; background: var(--peach); }
  .definition-text { left: 600px; top: 830px; width: 600px; text-align: center; font-family: "Fira Sans Condensed", sans-serif; font-weight: 600; font-size: 29px; color: var(--orange); }

  .footer-left { left: 0; top: 900px; width: 599px; height: 28px; background: var(--orange); }
  .footer-right { left: 601px; top: 900px; width: 599px; height: 28px; background: var(--orange); }
</style>
</head>
<body>
  <div class="block hello-band"></div>
  <h1 class="block hello-title">HELLO!</h1>
  <div class="block intro-panel"></div>
  <p class="block intro-name">My name is Margaret.</p>
  <div class="block intro-copy">
    <p>&nbsp;I offer simple, fun and insightful solutions to seemingly complicated clutter and organizational problems. I am here to help if you are ready to change your home and/or workspace.</p>
    <p>My experiences of working with family, friends, co-workers and clients has proven my hard working, energetic, fun and supportive attitude makes it easier for them to get things accomplished. Helping people sort through, and be rid of, the mental and physical obstacles that have kept them stuck along with participating in their enthusiasm when they see immediate improvement is rewarding for me.</p>
    <p>I welcome the opportunity to earn your confidence through ethical, reliable and dependable hard work.</p>
  </div>

  <div class="block card-panel"></div>
  <div class="block card-tab"></div>
  <p class="block card-tab-text">Organizing &amp; Decluttering Services</p>
  <p class="block card-name">Sunporch Tidy Works</p>
  <div class="block card-contact">
    <p>301-555-0148</p>
    <p>info@sunporchtidyworks.com</p>
    <p>www.sunporchtidyworks.com</p>
    <p>Fairhaven, MD</p>
  </div>

  <div class="block rule-orange"></div>
  <svg class="block member-badge" width="200" height="140" viewBox="0 0 200 140" role="img" aria-label="Professional association membership badge">
    <rect x="0" y="0" width="200" height="140" rx="10" fill="var(--badge)"/>
  </svg>
  <h2 class="block ethics-title">ETHICS:</h2>
  <p class="block ethics-copy">I abide by the standards as<br>outlined in the NGHO Code of Ethics.</p>
  <div class="block rule-peach"></div>

  <div class="block cover-panel"></div>
  <p class="block cover-name">Sunporch<br>Tidy Works</p>
  <div class="block cover-band"></div>
  <p class="block cover-band-text">Organizing &amp; Decluttering Services</p>
  <div class="block cover-contact-panel"></div>
  <div class="block cover-contact">
    <p>301-555-0148</p>
    <p class="gap">info@sunporchtidyworks.com</p>
    <p>www.sunporchtidyworks.com</p>
    <p class="gap">Fairhaven, MDServing MD, DC &amp; VA</p>
  </div>
  <div class="block cover-side"></div>
  <div class="block definition-panel"></div>
  <p class="block definition-text">Clarity: “The Quality or State of Being Clear”</p>

  <div class="block footer-left"></div>
  <div class="block footer-right"></div>
</body>
</html>
```